Business Stationery for Bramwell Oakes Recruitment Ltd
Marnie Thwaite
Cutting-Edge
Director
42 Quillmere Road
Teddington
Middlesex
KT4 9RW
marnie@bramwelloakes.co.uk
www.bramwelloakes.co.uk
Please use attached logo - I require the business card and company stationery - cutting edge design please

```html
<!DOCTYPE html>
<html lang="en">
<head>
<meta charset="utf-8">
<title>Bramwell Oakes Recruitment – Business Card</title>
<link rel="stylesheet" href="https://fonts.googleapis.com/css2?family=Cinzel:wght@400;600&family=Lato:wght@400;700&display=swap">
<style>
  :root {
    --navy: #26277a;
    --navy-deep: #17184f;
    --navy-light: #3a3c9c;
    --silver: #d9dbe4;
    --grey: #8a8c94;
    --paper: #ffffff;
    --backdrop: #e6e7ea;
  }
  * { margin: 0; padding: 0; box-sizing: border-box; }
  html, body { width: 1200px; height: 864px; overflow: hidden; }
  body {
    background: var(--backdrop);
    display: flex;
    align-items: center;
    justify-content: center;
    gap: 40px;
    font-family: "Lato", sans-serif;
  }
  .card {
    position: relative;
    width: 540px;
    height: 309px;
    border-radius: 18px;
    overflow: hidden;
    box-shadow: 0 10px 28px rgba(20, 20, 50, 0.22);
  }

  /* Card back */
  .card-back {
    background: radial-gradient(ellipse at 40% 35%, var(--navy-light), var(--navy) 55%, var(--navy-deep));
    display: flex;
    align-items: center;
    justify-content: center;
  }
  .back-name {
    font-family: "Cinzel", serif;
    font-weight: 400;
    font-size: 34px;
    letter-spacing: 3px;
    color: var(--silver);
  }
  .back-web {
    position: absolute;
    left: 26px;
    top: 50%;
    transform: translate(-50%, -50%) rotate(-90deg);
    font-size: 9px;
    letter-spacing: 3px;
    color: var(--silver);
    white-space: nowrap;
    text-transform: uppercase;
  }

  /* Card front */
  .card-front { background: var(--navy); }
  .front-shape { position: absolute; inset: 0; }
  .brand {
    position: absolute;
    left: 34px;
    top: 46px;
    font-family: "Cinzel", serif;
    font-weight: 600;
    color: var(--navy);
    line-height: 1.05;
  }
  .brand-name { font-size: 26px; letter-spacing: 1.5px; display: block; }
  .brand-line { font-size: 12px; letter-spacing: 6px; display: block; margin-top: 6px; }
  .person {
    position: absolute;
    left: 34px;
    top: 160px;
  }
  .person-name {
    font-family: "Cinzel", serif;
    font-weight: 600;
    font-size: 13px;
    letter-spacing: 2px;
    color: var(--navy);
  }
  .person-role {
    font-family: "Cinzel", serif;
    font-size: 9px;
    letter-spacing: 2px;
    color: var(--grey);
    margin-top: 3px;
  }
  .contact-list {
    position: absolute;
    right: 18px;
    top: 34px;
    list-style: none;
    color: var(--paper);
    font-size: 9px;
    letter-spacing: 0.3px;
  }
  .contact-list li {
    display: flex;
    align-items: center;
    justify-content: flex-end;
    gap: 6px;
    height: 16px;
    white-space: nowrap;
  }
  .contact-icon {
    width: 9px; height: 9px;
    border: 1px solid var(--paper);
    border-radius: 50%;
    flex: none;
  }
  .address {
    position: absolute;
    left: 34px;
    bottom: 12px;
    font-family: "Cinzel", serif;
    font-size: 9px;
    letter-spacing: 2px;
    color: var(--paper);
    line-height: 1.5;
  }
</style>
</head>
<body>

  <section class="card card-back" aria-label="Business card back">
    <span class="back-web">www.bramwelloakes.co.uk</span>
    <span class="back-name">Bramwell Oakes</span>
  </section>

  <section class="card card-front" aria-label="Business card front">
    <svg class="front-shape" viewBox="0 0 540 309" width="540" height="309" aria-hidden="true">
      <path d="M0 0 H300 C350 70 350 170 280 210 C220 240 120 244 0 240 Z" fill="var(--paper)"/>
      <path d="M314 0 C366 76 364 180 290 222 C226 256 120 258 0 254" fill="none" stroke="var(--grey)" stroke-width="6"/>
    </svg>

    <div class="brand">
      <span class="brand-name">Bramwell Oakes</span>
      <span class="brand-line">Recruitment</span>
    </div>

    <div class="person">
      <p class="person-name">Marnie Thwaite</p>
      <p class="person-role">Director</p>
    </div>

    <ul class="contact-list">
      <li>01632 960 482 <span class="contact-icon"></span></li>
      <li>07700 900 153 <span class="contact-icon"></span></li>
      <li>01632 960 719 <span class="contact-icon"></span></li>
      <li>marnie@bramwelloakes.co.uk <span class="contact-icon"></span></li>
      <li>www.bramwelloakes.co.uk <span class="contact-icon"></span></li>
    </ul>

    <p class="address">42 Quillmere Road, Teddington<br>Middlesex KT4 9RW</p>
  </section>

</body>
</html>
```